Modern book cover design

We are looking for a modern, powerful book cover for a general intrest book about how robots are going to take human jobs in the future.

The book title is "Torvanique"

It also has a strap line "The close of human work and how automatons will supplant it"
Both the title and the strap line should be on the front cover

I have attached a number of book designs I like, and my author picture.

Reason: Some great submissions but none quite have that wow factor

Target Market(s)

This is a general intrest book, but the reader is likely to be male 30-50

Requirements
Must have
• -Title "Torvanique"

-Strap-line "The close of human work and how automatons will supplant it"

-Be compliant with PrintMoraly Cover Design Criteria(www.printmoraly.example)

-Book size : 5.5 x 8.5 inches

-Spine size : 0.625 inches

-Must have one author picture on the back cover(attached)

-Must have the following author description on back cover:
"Tom Hollis is a leading futurologist, technologist, inventor, and entrepreneur. With over twenty years of experience in technology and innovation, Tom has travelled the world seeking out and developing new technologies. As a leading voice on the challenges and benefits of tomorrow’s technology, he has advised some of the world’s leading institutions, including the Grand Chancery, regarding technological preparations for the future. He is the recipient of the centennial founder of the season prize and has appeared on numerous technology and philanthropy television programs, as well as presenting Clever Little Marvels on Robotics."

-Must have the following book description on back cover:
“Torvanique is a look at the rapidly changing face of robotics and how it will revolutionize employment over the next thirty years. Tom Hollis lays out the arguments in favor of and against the mechanization of our society, as well as the advantages and untold risks as we march into this ever-present future.”

-Must have the following quote on the back cover:
"A fascinating look into the future of robotics and their impact on humanity, be prepared to question when robots will replace you - Derek Pallister, Professor of Cybernetics at the University of Castlemere”

-Example barcode

```html
<!DOCTYPE html>
<html lang="en">
<head>
<meta charset="utf-8">
<title>Torvanique – Book Cover</title>
<link rel="stylesheet" href="https://fonts.googleapis.com/css2?family=Arimo:ital,wght@0,400;0,700;1,400&family=Didact+Gothic&family=PT+Sans&display=swap">
<style>
  :root {
    --paper: #f1f1f1;
    --paper-grain: #e7e7e7;
    --ink: #111111;
    --ink-soft: #2a2a2a;
    --frame: #6f6f6f;
    --photo-light: #9a9a9a;
    --photo-dark: #3a3a3a;
    --accent-red: #d42a2a;
    --accent-grey: #c9c9c9;
  }
  * { margin: 0; padding: 0; box-sizing: border-box; }
  html, body { width: 1200px; height: 879px; overflow: hidden; }
  body { background: var(--paper); }

  .cover {
    position: relative;
    width: 1200px;
    height: 879px;
    overflow: hidden;
    background:
      radial-gradient(circle at 30% 40%, var(--paper-grain) 0 1px, transparent 1.5px) 0 0 / 6px 6px,
      var(--paper);
    color: var(--ink);
    font-family: "Arimo", Arial, sans-serif;
  }

  /* Back cover */
  .author-bio {
    position: absolute;
    left: 51px;
    top: 47px;
    width: 472px;
    font-size: 14px;
    line-height: 19.7px;
    color: var(--ink-soft);
  }
  .author-photo {
    float: left;
    width: 132px;
    height: 154px;
    margin: 6px 10px 0 0;
    background: linear-gradient(160deg, var(--photo-light), var(--photo-dark));
  }
  .bio-indent {
    float: right;
    width: 46px;
    height: 158px;
  }
  .book-summary {
    position: absolute;
    left: 53px;
    top: 350px;
    width: 492px;
    font-size: 12.8px;
    font-weight: 700;
    line-height: 23.4px;
  }
  .review {
    position: absolute;
    left: 54px;
    top: 660px;
    width: 500px;
    font-size: 12.8px;
    line-height: 23.4px;
  }
  .review-quote { font-weight: 700; }
  .review-source {
    font-style: italic;
    padding-left: 50px;
    line-height: 20px;
    color: var(--ink-soft);
  }
  .barcode-area {
    position: absolute;
    left: 440px;
    top: 792px;
    width: 104px;
    height: 61px;
    border: 1px solid var(--frame);
    background: #ffffff;
  }

  /* Spine */
  .spine-text {
    position: absolute;
    white-space: nowrap;
    font-weight: 400;
    transform: rotate(-90deg);
    transform-origin: left top;
    color: var(--ink);
  }
  .spine-title {
    left: 568px;
    top: 702px;
    font-family: "Didact Gothic", "Century Gothic", sans-serif;
    font-size: 53px;
    line-height: 56px;
  }
  .spine-author {
    left: 580px;
    top: 314px;
    font-family: "PT Sans", Tahoma, sans-serif;
    font-size: 29px;
    line-height: 32px;
  }

  /* Front cover */
  .front-title {
    position: absolute;
    right: 124px;
    top: 682px;
    font-family: "PT Sans", Tahoma, sans-serif;
    font-size: 33px;
    font-weight: 400;
    text-shadow: 1px 1px 2px rgba(0,0,0,0.35);
  }
  .front-strapline {
    position: absolute;
    right: 118px;
    top: 724px;
    font-family: "PT Sans", Tahoma, sans-serif;
    font-size: 16px;
    text-shadow: 1px 1px 1px rgba(0,0,0,0.2);
  }
  .button-artwork {
    position: absolute;
    left: 1063px;
    top: 747px;
    width: 93px;
    height: 82px;
    background: linear-gradient(180deg, var(--accent-red) 0%, var(--accent-red) 55%, var(--accent-grey) 100%);
  }
</style>
</head>
<body>
<main class="cover">
  <section class="back-cover">
    <p class="author-bio">
      <span class="author-photo" role="img" aria-label="Black and white portrait photo of the author, Tom Hollis"></span>
      <span class="bio-indent" aria-hidden="true"></span>
      Tom Hollis is a leading futurologist, technologist, inventor, and entrepreneur. With over twenty years of experience in technology and innovation, Tom has travelled the world seeking out and developing new technologies. As a leading voice on the challenges and benefits of tomorrow’s technology, he has advised some of the world’s leading institutions, including the Grand Chancery, regarding technological preparations for the future. He is the recipient of the centennial founder of the season prize and has appeared on numerous technology and philanthropy television programs, as well as presenting Clever Little Marvels on Robotics.
    </p>

    <p class="book-summary">
      Torvanique is a look at the rapidly changing face of robotics and how it will revolutionize employment over the next thirty years. Tom Hollis lays out the arguments in favor of and against the mechanization of our society, as well as the advantages and untold risks as we march into this ever-present future.
    </p>

    <blockquote class="review">
      <p class="review-quote">"A fascinating look into the future of robotics and their impact on humanity, be prepared to question when robots will replace you "</p>
      <p class="review-source">Derek Pallister, Professor of Cybernetics at the University of Castlemere.</p>
    </blockquote>

    <div class="barcode-area" aria-hidden="true"></div>
  </section>

  <section class="spine">
    <h2 class="spine-text spine-title">Torvanique</h2>
    <p class="spine-text spine-author">Tom Hollis</p>
  </section>

  <section class="front-cover">
    <h1 class="front-title">Torvanique</h1>
    <p class="front-strapline">The close of human work and how automatons will supplant it..</p>
    <div class="button-artwork" role="img" aria-label="Illustration of a glossy red push button labelled push"></div>
  </section>
</main>
</body>
</html>
```